Vesprine Oakville Cabernet Sauvignon-Wine label design

We need a package design for an up market wine brand named, Vesprine. It will be a Cabernet Sauvignon from the Oakville AVA of Napa Valley. We are looking for a stylish modern label that will stand out on a retail shelf. We want the label to be attention grabbing and stylish while presenting an up market luxury brand.

Sick

Requirements
Must have
• Must have the words(in order of importance)
-Vesprine
-Cabernet Sauvignon
-Oakville
-Napa Valley
-2018

Must be designed for a traditional "Bordeaux" style bottle (Bottle specs in uploaded files)
Should not have
• Any images of grapes, vineyards, wine glasses or bottles

```html
<!DOCTYPE html>
<html lang="en">
<head>
<meta charset="UTF-8">
<title>Vesprine Cabernet Sauvignon Label</title>
<link rel="stylesheet" href="https://fonts.googleapis.com/css2?family=Montserrat:wght@300;400;600&display=swap">
<style>
  :root {
    --backdrop: #1a1a1a;
    --paper: #f7f7f5;
    --label-dark: #2b2b2b;
    --silver: #dcdcdc;
    --gold-deep: #8a6a1c;
    --gold-mid: #d9b24a;
    --gold-light: #f3dc8a;
    --tree-haze: rgba(156, 191, 74, 0);
    --tree-light: rgba(156, 191, 74, 0.28);
    --tree-mid: rgba(95, 143, 44, 0.45);
    --tree-ground: #c9b36a;
  }
  * { margin: 0; padding: 0; box-sizing: border-box; }
  html, body {
    width: 801px;
    height: 1200px;
    overflow: hidden;
    background: var(--backdrop);
  }
  .canvas {
    position: relative;
    width: 801px;
    height: 1200px;
    font-family: "Montserrat", sans-serif;
  }
  .label {
    position: absolute;
    left: 40px;
    top: 158px;
    width: 721px;
    height: 884px;
    overflow: hidden;
  }
  .label__top {
    position: absolute;
    left: 0; top: 0;
    width: 100%;
    height: 336px;
    background: var(--paper);
  }
  .label__artwork {
    position: absolute;
    left: 140px;
    top: 100px;
    width: 414px;
    height: 236px;
    background:
      linear-gradient(180deg, var(--tree-haze) 0%, var(--tree-light) 45%, var(--tree-mid) 92%, var(--tree-ground) 100%);
  }
  .label__band {
    position: absolute;
    left: 0; top: 336px;
    width: 100%;
    height: 35px;
    background: linear-gradient(90deg, var(--gold-deep) 0%, var(--gold-mid) 30%, var(--gold-light) 55%, var(--gold-mid) 75%, var(--gold-deep) 100%);
  }
  .label__bottom {
    position: absolute;
    left: 0; top: 371px;
    width: 100%;
    height: 513px;
    background: var(--label-dark);
  }
  .text {
    position: absolute;
    left: 145px;
    line-height: 1;
    color: var(--silver);
    white-space: nowrap;
  }
  .brand-name {
    top: 436px;
    font-size: 76px;
    font-weight: 400;
    letter-spacing: 6px;
  }
  .varietal {
    top: 551px;
    left: 148px;
    font-size: 23px;
    font-weight: 600;
    letter-spacing: 3.4px;
  }
  .appellation {
    top: 729px;
    font-size: 33px;
    font-weight: 300;
    letter-spacing: 6px;
  }
  .region {
    top: 777px;
    font-size: 32px;
    font-weight: 300;
    letter-spacing: 3.5px;
  }
  .vintage {
    top: 821px;
    font-size: 29px;
    font-weight: 600;
    letter-spacing: 9px;
  }
  .rule {
    position: absolute;
    left: 147px;
    top: 864px;
    width: 356px;
    height: 1px;
    background: var(--silver);
    opacity: 0.7;
  }
</style>
</head>
<body>
  <main class="canvas">
    <section class="label">
      <div class="label__top"></div>
      <div class="label__artwork" role="img" aria-label="Illustration of a light row of tall slender cypress trees in shades of green on a thin ground line"></div>
      <div class="label__band"></div>
      <div class="label__bottom"></div>
      <h1 class="text brand-name">VESPRINE</h1>
      <p class="text varietal">CABERNET SAUVIGNON</p>
      <p class="text appellation">OAKVILLE</p>
      <p class="text region">Napa Valley</p>
      <p class="text vintage">2018</p>
      <div class="rule"></div>
    </section>
  </main>
</body>
</html>
```